Hurricane Damage Public Adjuster Billboard

I have created several projects with you and have several great designs. I need to format them into a Billboard for upcoming Hurricane Season. Need done in a month. Im also in process of getting an eye catching and easy to remember 800# Vanity phone number like Call 800-Stormsafe or 800- Need Help? My included past Pixel Bazaar projects will give you an idea of what colors, schemes, and designs I gravitate towards. 3 past Design projects were 1) 2 Logos where I picked the 1st place and the 2nd place and 2) Index Card where I picked the winner as the Index Card and the 2nd place as a Post Card. Point is, I will pick and pay for 2 winners if they're good. This should help to sweeten the pot. Also, please look at my website for ideas that I like:

www.CedarlineClaimHelp.com
I want people to feel that I am the best and highest. Level.

I've been getting a lot of quick half effort designs basically cut & pasting my previous projects. Please don't rush and take your time to be creative. A an example, my Biggest Competitor is Tamarack Public Adjusting. Their colors are Black and Gold while mine are Blue, White, and Black with a highlight of Orange if possible. I JUST imported a picture of their BillBoard. I need mine better and BLOW AWAY THEIRS. Terms like "Don't be Victimized Twice ?, Don't let the Hurricane Ruin your Life?". "Get Fairly Paid & Move On" "Our Clients Claims are VIP?
Updates

I'm getting a lot of quick half effort ones. I'd rather you take your time and really put some thoughts and effort into it. My Biggest Competitor is Tamarack Public Adjusting. They have black & gold colors, while I have Blue, Black, and white.

It needs to blow theirs away. I have imported their Billboard for comparative purposes.

Guy's,
I'll make it easier for you in what I'm looking for. Please look at the Tamarack Billboard picture attached.

1) Put my "Blue Shield" to the left, replacing their logo
2) change color patterns from their (Black, Gold, White) to my color schemes of (Black, Blue, White)
3) I want to see my name where their is:

THE
Cedarline Claim Help
EXPERT & LOCAL Public Adjusters
"FOR THE POLICYHOLDER!!"

4) to the right, add the A+Rated logo and QRT+ Accredited logo, 5 Star Zorvex Rated logo, 5 Start PORCHLINK Highly Rated logo, etc..

5) the right side is where you can be creative as I will not have a picture of me there.

"20+ Years of Experience, Recovering Millions for our VIP Clients"

"Your Best, Locally-Based Private Adjuster & Advocate'
"FOR THE POLICYHOLDER!!"

"Don't be victimized Twice!!"

"Don't let the Hurricane Ruin Your Life!!"

This should really help. Also, refer to my website, maybe a couple testimonial fillers?

Thanks all,

marcus@CedarlineClaimHelp.com

Just imported a few awards that would look great to the right side with all the other 5 Star Ratings and accolades.
This right section could be titled like zmy Website:

5 Star Reviews, Ratings & Awards:
4-5 Logos underneath?

Target Market(s)

Coastal place where a Hurricane 🌀 🌀 Hits

Industry/Entity Type

Hurricane Public Insurance Adjuster

Font styles to use
Sans Serif
Other font styles liked:
• Zurich fonts

Colors
0054AA
0677BA
7BADD7
CADEEF
E8F1F8
EE7325
F08F49
F5BC92
FAE3D3
FDF4ED

Requirements
Must have
• Use my past project logos, colors, and schemes to create eye grabbing BillBoard
Nice to have
Should not have
• Not be too busy, must be Easy to Read, Eye Catchy

```html
<!DOCTYPE html>
<html lang="en">
<head>
<meta charset="utf-8">
<title>Cedarline Claim Help Billboard</title>
<link rel="stylesheet" href="https://fonts.googleapis.com/css2?family=Oswald:wght@600&family=Poppins:ital,wght@0,500;0,700;1,700&display=swap">
<style>
  :root {
    --backdrop: #bdbdbd;
    --navy-deep: #062338;
    --navy: #0a3e5c;
    --blue-band: #0677BA;
    --blue-bright: #1aa3e8;
    --blue-brand: #0054AA;
    --blue-sky: #0a9be0;
    --orange: #F5922F;
    --white: #ffffff;
    --red: #e3201b;
    --green: #86cf16;
    --star: #f5a623;
    --ink-navy: #103a5a;
  }
  * { box-sizing: border-box; margin: 0; padding: 0; }
  html, body { width: 1200px; height: 869px; overflow: hidden; }
  body { background: var(--backdrop); position: relative; font-family: "Poppins", sans-serif; }

  .billboard {
    position: absolute; left: 76px; top: 282px;
    width: 1048px; height: 305px;
    background: var(--white); overflow: hidden;
  }
  .hero-band {
    position: absolute; left: 0; top: 0; width: 1048px; height: 208px;
    background: linear-gradient(90deg, var(--navy-deep) 0%, var(--navy) 45%, #0b4f74 100%);
  }
  .advocate-band {
    position: absolute; left: 0; top: 117px; width: 1048px; height: 91px;
    background: linear-gradient(90deg, rgba(6,119,186,0) 15%, #0a6fa8 45%, var(--blue-band) 100%);
  }
  .storm-art {
    position: absolute; left: 683px; top: 0; width: 144px; height: 118px;
    background: radial-gradient(ellipse at 50% 40%, rgba(150,130,230,0.55) 0%, rgba(90,80,170,0.25) 45%, rgba(10,62,92,0) 75%);
  }

  .brand-mark {
    position: absolute; left: 40px; top: 60px; width: 150px;
    display: flex; flex-direction: column; align-items: center; gap: 10px;
  }
  .brand-mark .mark-square { width: 34px; height: 34px; background: var(--blue-bright); }
  .brand-mark .mark-name {
    color: var(--blue-bright); font-weight: 700; font-size: 21px;
    line-height: 1.15; text-align: center;
  }

  .headline-lead {
    position: absolute; left: 203px; top: 28px;
    color: var(--white); font-weight: 500; font-size: 30px; line-height: 1;
  }
  .headline-main {
    position: absolute; left: 203px; top: 62px;
    color: var(--orange); font-family: "Oswald", sans-serif; font-weight: 600;
    font-size: 48px; line-height: 1; letter-spacing: -0.5px;
  }
  .tagline {
    position: absolute; left: 202px; top: 123px;
    color: var(--white); font-style: italic; font-weight: 700;
    font-size: 34px; line-height: 38px; letter-spacing: -0.3px;
  }

  .phone {
    position: absolute; left: 33px; top: 221px;
    display: flex; align-items: center; gap: 18px;
  }
  .phone-icon { width: 54px; height: 54px; }
  .phone-number {
    color: var(--orange); font-family: "Oswald", sans-serif; font-weight: 600;
    font-size: 64px; line-height: 1; letter-spacing: -0.5px;
  }
  .divider {
    position: absolute; left: 507px; top: 218px; width: 1px; height: 60px;
    background: #9aa5ad;
  }
  .award {
    position: absolute; left: 540px; top: 224px;
    font-weight: 700; font-size: 25px; line-height: 29px; color: var(--blue-brand);
  }
  .award .accent { color: var(--blue-sky); }

  .ratings-panel { position: absolute; left: 0; top: 0; }

  .ratings {
    position: absolute; left: 860px; top: 32px; width: 162px;
    display: flex; flex-direction: column; align-items: center;
  }
  .rating-title { color: var(--red); font-weight: 700; font-size: 28px; line-height: 1; }
  .accredit-badge {
    margin-top: 20px; width: 130px; height: 48px;
    background: var(--ink-navy); border-radius: 5px;
  }
  .accredit-note { margin-top: 4px; color: var(--ink-navy); font-weight: 700; font-size: 10.5px; }
  .review-name { margin-top: 10px; color: var(--blue-band); font-weight: 700; font-size: 34px; line-height: 1; }
  .stars { margin-top: 2px; display: flex; gap: 2px; }
  .stars svg { width: 17px; height: 17px; }
  .community-name { margin-top: 16px; color: var(--green); font-weight: 700; font-size: 24px; line-height: 1; }
</style>
</head>
<body>
  <div class="billboard">
    <div class="hero-band"></div>
    <div class="advocate-band"></div>
    <div class="storm-art" role="img" aria-label="Lightning bolt striking across the stormy sky"></div>

    <div class="brand-mark">
      <div class="mark-square"></div>
      <div class="mark-name">Cedarline<br>Claim Help</div>
    </div>

    <div class="headline-lead">DON'T LET THE</div>
    <div class="headline-main">HURRICANE RUIN YOUR LIFE !</div>
    <div class="tagline">CEDARLINE CLAIM HELP<br>EXPERT PUBLIC ADJUSTERS</div>

    <div class="phone">
      <svg class="phone-icon" viewBox="0 0 54 54" aria-hidden="true">
        <circle cx="27" cy="27" r="27" fill="#0a3e5c"/>
        <path d="M19 15c1.5-1 3-.8 3.8.6l2.6 4.4c.7 1.2.3 2.6-.8 3.3l-1.6 1c1 2.6 3.2 5 5.8 6.3l1.1-1.5c.8-1.1 2.2-1.3 3.3-.5l4.2 2.8c1.3.9 1.4 2.4.3 3.8-1.7 2.2-4 3.2-6.4 2.4C23.6 36.4 17.4 30 15.6 22.4c-.6-2.7.9-5.6 3.4-7.4z" fill="#fff"/>
        <path d="M29 15.5a9 9 0 0 1 9 9" stroke="#fff" stroke-width="2.2" fill="none" stroke-linecap="round"/>
        <path d="M29 20a4.5 4.5 0 0 1 4.5 4.5" stroke="#fff" stroke-width="2.2" fill="none" stroke-linecap="round"/>
      </svg>
      <div class="phone-number">855-FAIR DEAL</div>
    </div>
    <div class="divider"></div>
    <div class="award">
      VOTED <span class="accent">2022 BEST</span><br>
      PUBLIC <span class="accent">ADJUSTER</span>
    </div>

    <svg class="ratings-panel" width="1048" height="305" viewBox="0 0 1048 305" aria-hidden="true">
      <defs>
        <linearGradient id="arcStroke" x1="0" y1="0" x2="0" y2="1">
          <stop offset="0" stop-color="#1aa3e8"/>
          <stop offset="1" stop-color="#0677BA"/>
        </linearGradient>
      </defs>
      <path d="M925,0 H1048 V305 H915 C845,262 806,222 808,166 C810,100 860,32 925,0 Z" fill="#ffffff"/>
      <path d="M925,0 C860,32 810,100 808,166 C806,222 845,262 915,305" fill="none" stroke="url(#arcStroke)" stroke-width="14"/>
    </svg>

    <div class="ratings">
      <div class="rating-title">A+ Rating</div>
      <div class="accredit-badge"></div>
      <div class="accredit-note">QRT Rating: A+</div>
      <div class="review-name">Zorvex</div>
      <div class="stars">
        <svg viewBox="0 0 24 24"><path d="M12 2l2.9 6.6 7.1.6-5.4 4.7 1.6 7L12 17.3 5.8 20.9l1.6-7L2 9.2l7.1-.6z" fill="#f5a623"/></svg>
        <svg viewBox="0 0 24 24"><path d="M12 2l2.9 6.6 7.1.6-5.4 4.7 1.6 7L12 17.3 5.8 20.9l1.6-7L2 9.2l7.1-.6z" fill="#f5a623"/></svg>
        <svg viewBox="0 0 24 24"><path d="M12 2l2.9 6.6 7.1.6-5.4 4.7 1.6 7L12 17.3 5.8 20.9l1.6-7L2 9.2l7.1-.6z" fill="#f5a623"/></svg>
        <svg viewBox="0 0 24 24"><path d="M12 2l2.9 6.6 7.1.6-5.4 4.7 1.6 7L12 17.3 5.8 20.9l1.6-7L2 9.2l7.1-.6z" fill="#f5a623"/></svg>
        <svg viewBox="0 0 24 24"><path d="M12 2l2.9 6.6 7.1.6-5.4 4.7 1.6 7L12 17.3 5.8 20.9l1.6-7L2 9.2l7.1-.6z" fill="#f5a623"/></svg>
      </div>
      <div class="community-name">PORCHLINK</div>
    </div>
  </div>
</body>
</html>
```